Sollavern Letterhead and Template Design

We are looking to freshen up and modernise our business letter heads and cover pages for our documents. Looking at a suit of new designs. I would like a design for:
- Letter Head
- Page 2 follower (for lengthy documents) - fancy
- Page 2 follower (for lengthy documents) - simple version
- Cover Page for reports to sent to client
- Cover Page for internal documents.

Our website is www.sollavern.com.au.

I have attached a copy of our current brochure for inspiration and our old letter head so you can see what we currently use.

On our Client Cover Page and letter head we would like to include out business awards. Happy for you to change these designs if you have something that would look better. Have also included logos and awards. We won the National Bugcare Leader Prize in 2022/23 and also in 2019/2020. We were a state finalist in the Korimbo Trade Honours this year logo attached.

We like the emblem to be watermarked into the page in the background.

We want something fresh/clean/modern and classy.

Letter head needs to include our Phone Number: 1300951736
Email: hello@sollavern.com.au
Text: 0477193508
Website: www.sollavern.com.au

```html
<!DOCTYPE html>
<html lang="en">
<head>
<meta charset="utf-8">
<title>Sollavern Letterhead</title>
<link href="https://fonts.googleapis.com/css2?family=Lato:wght@400;700&display=swap" rel="stylesheet">
<style>
  :root {
    --backdrop: #dbdbdb;
    --paper: #ffffff;
    --ink: #1f1f1f;
    --brand-dark: #3d3d3d;
    --brand-green: #7ac143;
    --watermark: #e5e5e5;
    --badge-gold: #d9b25a;
    --badge-dark: #2b2b2b;
  }
  * { margin: 0; padding: 0; box-sizing: border-box; }
  html, body {
    width: 1200px;
    height: 947px;
    overflow: hidden;
    background: var(--backdrop);
    font-family: "Lato", sans-serif;
  }
  .letterhead {
    position: absolute;
    left: 364px;
    top: 179px;
    width: 472px;
    height: 605px;
    background: var(--paper);
  }
  .brand {
    position: absolute;
    left: 46px;
    top: 22px;
    height: 40px;
    display: flex;
    align-items: center;
    gap: 8px;
  }
  .brand-dot {
    width: 16px;
    height: 16px;
    border-radius: 50%;
    background: var(--brand-green);
  }
  .brand-name {
    font-weight: 700;
    font-size: 29px;
    letter-spacing: 0.3px;
    color: var(--brand-dark);
  }
  .contact {
    position: absolute;
    right: 46px;
    top: 15px;
    list-style: none;
    text-align: right;
    font-size: 9.2px;
    line-height: 11px;
    color: var(--ink);
  }
  .contact li {
    display: flex;
    justify-content: flex-end;
    align-items: center;
    gap: 4px;
  }
  .contact svg {
    width: 8px;
    height: 8px;
    flex: none;
  }
  .watermark {
    position: absolute;
    left: 130px;
    top: 129px;
    width: 213px;
    height: 247px;
    border-radius: 50%;
    background: var(--watermark);
  }
  .awards {
    position: absolute;
    left: 0;
    right: 0;
    top: 539px;
    display: flex;
    justify-content: center;
    align-items: flex-start;
    gap: 22px;
    padding-left: 8px;
  }
  .award-seal { width: 52px; height: 52px; }
  .award-shield { width: 30px; height: 38px; margin-top: 5px; }
</style>
</head>
<body>
  <main class="letterhead">
    <header>
      <div class="brand">
        <span class="brand-dot"></span>
        <span class="brand-name">Sollavern</span>
      </div>
      <ul class="contact">
        <li>1300951736
          <svg viewBox="0 0 10 10" aria-hidden="true"><path d="M2 1 L4 1 L4.6 3 L3.4 4 Q4.5 6 6 6.6 L7 5.4 L9 6 L9 8 Q5 9 1 2 Z" fill="var(--brand-green)"/></svg>
        </li>
        <li>0477193508
          <svg viewBox="0 0 10 10" aria-hidden="true"><rect x="2.5" y="1" width="5" height="2.5" fill="var(--brand-green)"/><rect x="1" y="3.5" width="8" height="3.5" rx="0.8" fill="var(--brand-green)"/><rect x="2.5" y="6" width="5" height="3" fill="var(--brand-green)"/></svg>
        </li>
        <li>hello@sollavern.com.au
          <svg viewBox="0 0 10 10" aria-hidden="true"><rect x="0.5" y="2" width="9" height="6.5" fill="var(--brand-green)"/><path d="M0.8 2.3 L5 5.8 L9.2 2.3" stroke="#fff" stroke-width="0.8" fill="none"/></svg>
        </li>
        <li>www.sollavern.com.au
          <svg viewBox="0 0 10 10" aria-hidden="true"><circle cx="5" cy="5" r="4.3" fill="var(--brand-green)"/><path d="M0.7 5 H9.3 M5 0.7 V9.3 M1.5 3 H8.5 M1.5 7 H8.5" stroke="#fff" stroke-width="0.5"/><ellipse cx="5" cy="5" rx="2" ry="4.3" fill="none" stroke="#fff" stroke-width="0.5"/></svg>
        </li>
      </ul>
    </header>

    <div class="watermark" role="img" aria-label="Large faint brand emblem watermark"></div>

    <footer class="awards">
      <svg class="award-seal" viewBox="0 0 52 52" role="img" aria-label="National Bugcare Leader Prize award badge">
        <circle cx="26" cy="26" r="25" fill="var(--badge-gold)"/>
      </svg>
      <svg class="award-shield" viewBox="0 0 30 38" role="img" aria-label="Industry award badge">
        <path d="M1 1 H29 V20 Q29 32 15 37 Q1 32 1 20 Z" fill="var(--badge-dark)"/>
      </svg>
    </footer>
  </main>
</body>
</html>
```